Mend and secure Word doc project

Mend & Secure are an established home appliance repair and warranty provider looking to rebrand the letters sent to our customers with a new and fresh design.
Please refer to our website for our colour scheme and logo which we are not looking to change:
www.mendandsecure-example.co.uk
The letters which we are looking to have redesigned are:
Welcome letters / confirmation paperwork
Basic letter template
Welcome letters:
Page 1 – Opening / Welcome
Page 2 – Plan documentation details
Page 3 & 4 – Terms & Conditions
We can provide a copy of our current welcome / confirmation letters but as we are looking for full redesign, we are looking to steer away from what we have been using historically.
We will be running further projects and we are looking to use the same designer which we pick from this competition so please consider this when submitting your designs.
UPDATE - 01/11/23
An example of our current Welcome documentation has been uploaded for the purpose of example of the placement of the content. As per the brief, we are not looking for a similar design but purely uploading the current documentation to give you an idea of what we are currently using.
Look and feel
Each slider illustrates characteristics of the customer's brand and the style your logo design should communicate.

```html
<!DOCTYPE html>
<html lang="en">
<head>
<meta charset="utf-8">
<title>Mend &amp; Secure – Documentation Details</title>
<link href="https://fonts.googleapis.com/css2?family=Montserrat:wght@400&family=Poppins:wght@300;400;700&display=swap" rel="stylesheet">
<style>
  :root {
    --navy: #1b4f7e;
    --heading-blue: #1f9fc6;
    --heading-teal: #22c3d0;
    --body-grey: #7a7a7a;
    --quote-grey: #878787;
    --bubble-light: #daedf4;
    --bubble-teal: #1ecfd6;
    --footer-a: #1a82a8;
    --footer-b: #2aa4c9;
    --white: #ffffff;
  }
  * { margin: 0; padding: 0; box-sizing: border-box; }
  html, body { width: 1200px; height: 675px; overflow: hidden; background: var(--white); }
  body { position: relative; font-family: "Poppins", sans-serif; }

  .page { position: absolute; top: 0; width: 470px; height: 675px; }
  .page--details { left: 101px; }
  .page--testimonials { left: 637px; }

  .page-header {
    position: absolute; left: 0; top: 0; width: 470px; height: 78px;
    background: linear-gradient(100deg, #d9edf5 0%, #d4f6f6 55%, #e4fbf1 100%);
  }
  .page-title {
    position: absolute; left: 36px; top: 33px;
    font-family: "Montserrat", sans-serif; font-weight: 400;
    font-size: 18px; letter-spacing: 0.8px; color: var(--navy); line-height: 1;
  }
  .page-subtitle {
    position: absolute; left: 37px; top: 55px;
    font-family: "Montserrat", sans-serif; font-weight: 400;
    font-size: 9px; letter-spacing: 0.5px; color: #3b77a3; line-height: 1;
  }

  .section { position: absolute; left: 36px; width: 400px; }
  .section--one { top: 110px; }
  .section--two { top: 289px; }
  .section-heading {
    font-family: "Montserrat", sans-serif; font-weight: 400;
    font-size: 10px; letter-spacing: 1.4px; line-height: 12px;
    color: var(--heading-blue); margin-bottom: 13px;
  }
  .section--two .section-heading { color: var(--heading-teal); }
  .section-text {
    font-weight: 300; font-size: 9.1px; line-height: 16.1px;
    color: var(--body-grey); margin-bottom: 16px;
  }

  .page-footer {
    position: absolute; left: 0; top: 623px; width: 470px; height: 52px;
    background: linear-gradient(90deg, var(--footer-a) 0%, var(--footer-b) 100%);
  }
  .footer-copy {
    position: absolute; left: 34px; top: 21px;
    font-weight: 300; font-size: 8.4px; color: var(--white); line-height: 1;
  }
  .footer-brand {
    position: absolute; right: 22px; top: 14px;
    display: flex; flex-direction: column; align-items: center; gap: 4px;
  }
  .footer-brand-dot { width: 12px; height: 12px; border-radius: 50%; background: var(--white); }
  .footer-brand-name {
    font-weight: 400; font-size: 7.5px; letter-spacing: 0.4px;
    color: var(--white); line-height: 1;
  }

  .bubbles { position: absolute; left: 0; top: 0; }
  .quote {
    position: absolute; font-size: 14.6px; line-height: 17px; font-weight: 400;
  }
  .quote--light { left: 72px; top: 255px; width: 120px; color: var(--quote-grey); }
  .quote--teal { left: 250px; top: 260px; width: 138px; text-align: right; color: var(--white); }
  .quote-author { font-weight: 700; font-size: 14.6px; line-height: 17px; position: absolute; }
  .quote-author--light { left: 72px; top: 353px; color: var(--navy); }
  .quote-author--teal { left: 286px; top: 327px; color: var(--white); }
</style>
</head>
<body>

<section class="page page--details">
  <header class="page-header">
    <h1 class="page-title">DOCUMENTATION</h1>
    <p class="page-subtitle">DETAILS</p>
  </header>

  <div class="section section--one">
    <h2 class="section-heading">HEADING 1</h2>
    <p class="section-text">Lorem ipsum dolor sit amet, consectetur adipiscing elit, sed do eiusmod tempor incididunt ut labore et dolore magna aliqua. Ut enim ad minim veniam, quis nostrud exercitation ullamco laboris nisi ut aliquip ex ea commodo consequat.</p>
    <p class="section-text">Duis aute irure dolor in reprehenderit in voluptate velit esse cillum dolore eu fugiat nulla pariatur. Excepteur sint occaecat cupidatat non proident, sunt in culpa qui officia deserunt mollit anim id est laborum</p>
  </div>

  <div class="section section--two">
    <h2 class="section-heading">HEADING 2</h2>
    <p class="section-text">Lorem ipsum dolor sit amet, consectetur adipiscing elit, sed do eiusmod tempor incididunt ut labore et dolore magna aliqua. Ut enim ad minim veniam, quis nostrud exercitation ullamco laboris nisi ut aliquip ex ea commodo consequat.</p>
    <p class="section-text">Duis aute irure dolor in reprehenderit in voluptate velit esse cillum dolore eu fugiat nulla pariatur. Excepteur sint occaecat cupidatat non proident, sunt in culpa qui officia deserunt mollit anim id est laborum</p>
  </div>

  <footer class="page-footer">
    <p class="footer-copy">© 2023, Copyright © 2023 Mend &amp; Secure LTD</p>
    <div class="footer-brand">
      <span class="footer-brand-dot"></span>
      <span class="footer-brand-name">MEND &amp; SECURE</span>
    </div>
  </footer>
</section>

<section class="page page--testimonials">
  <svg class="bubbles" width="470" height="675" viewBox="0 0 470 675" aria-hidden="true">
    <path d="M153 131 L153 187 A113 113 0 1 1 63 219 Z" fill="var(--bubble-light)"/>
    <path d="M315 470 L315 413 A114 114 0 1 1 403 380 Z" fill="var(--bubble-teal)"/>
  </svg>

  <p class="quote quote--light">Fast, reliable we’re so pleased, thank you!</p>
  <p class="quote-author quote-author--light">Ava, Northampton</p>

  <p class="quote quote--teal">Fast, reliable we’re so pleased, thank you!</p>
  <p class="quote-author quote-author--teal">Ben, Brighton</p>

  <footer class="page-footer">
    <p class="footer-copy">© 2023, Copyright © 2023 Mend &amp; Secure LTD</p>
    <div class="footer-brand">
      <span class="footer-brand-dot"></span>
      <span class="footer-brand-name">MEND &amp; SECURE</span>
    </div>
  </footer>
</section>

</body>
</html>
```